Copper Ridge Resort & Marina - Boat Slips, Cabin Rentals, Floating Vacation Homes, & More

We need an 8'H x 16'W billboard for our Resort & marina, www.copperridgeresort.example. We'd like it to include: Lakefront Cabin Rentals, Floating Vacation Homes, and New Slips Summer 2022. We'd like it to be simple using the colors on our logo, similar to our business cards, and have our logo on it large. Maybe an arrow on the bottom pointing left that says 3 miles, possibly our website and phone number.

Target Market(s)

Lake People, Boaters

Industry/Entity Type

Resort & Marina (Recreation/Hospitality)

Font styles to use
Sans Serif
Other font styles liked:
• Simple/modern

Colors
0054AA
0677BA
7BADD7
CADEEF
E8F1F8
FFC000
F8CF3A
FAE287
FDF2CF
FEFAEE
F0912C
F2A743
F7CA91
FBE8D2
FDF5EE

Requirements
Must have
• Logo, Cabin Rentals, Floating Vacation Homes, New Slips Summer 2022
Nice to have
• An additional banner hanging from the bottom with an orange (or blue, colors from our logo) arrow pointing left, with white text saying: 3 miles 555-214-0867 www.copperridgeresort.example
Should not have
• Shouldn't be too busy

```html
<!DOCTYPE html>
<html lang="en">
<head>
<meta charset="utf-8">
<title>Copper Ridge Resort &amp; Marina – Billboard</title>
<link href="https://fonts.googleapis.com/css2?family=Roboto:wght@700;900&display=swap" rel="stylesheet">
<style>
  :root {
    --navy: #1b4a86;
    --sun-yellow: #f8b824;
    --sun-orange: #f0912c;
    --flame: #e8533a;
    --white: #ffffff;
    --sky-pale: #e8f1f8;
    --lake-light: #cadeef;
    --lake-mid: #7badd7;
  }
  * { margin: 0; padding: 0; box-sizing: border-box; }
  html, body { width: 1200px; height: 675px; overflow: hidden; background: var(--sky-pale); }
  body { font-family: "Roboto", Arial, sans-serif; }

  .billboard {
    position: absolute;
    left: 0; top: 37.5px;
    width: 1200px; height: 600px;
    background: var(--white);
    overflow: hidden;
  }

  .brand-mark {
    position: absolute;
    left: 325px; top: 40px;
    width: 80px; height: 80px;
    border-radius: 50%;
    background: var(--sun-orange);
  }
  .brand-name {
    position: absolute;
    left: 60px; top: 150px;
    width: 610px;
    text-align: center;
    color: var(--navy);
    font-weight: 700;
    line-height: 1;
  }
  .brand-name .line-main { display: block; font-size: 66px; letter-spacing: 1px; }
  .brand-name .line-sub { display: block; font-size: 28px; letter-spacing: 8px; margin-top: 12px; }

  .phone {
    position: absolute;
    left: 60px; top: 298px;
    width: 610px;
    text-align: center;
    color: var(--navy);
    font-size: 68px;
    font-weight: 700;
    letter-spacing: 1px;
  }

  .lake-map {
    position: absolute;
    left: 690px; top: 10px;
    width: 500px; height: 440px;
    background: linear-gradient(135deg, var(--lake-light), var(--lake-mid));
    border-radius: 6px;
  }

  .distance {
    position: absolute;
    left: 160px; top: 437px;
    color: var(--navy);
    font-size: 33px;
    font-weight: 900;
  }

  .direction-stripes {
    position: absolute;
    left: 0; top: 489px;
    width: 410px; height: 28px;
    background: repeating-linear-gradient(-60deg,
      var(--sun-yellow) 0 14px, var(--white) 14px 24px);
  }
  .direction-arrow { position: absolute; left: 405px; top: 432px; }

  .web-bar {
    position: absolute;
    left: 468px; top: 461px;
    width: 732px; height: 52px;
    background: var(--flame);
    color: var(--white);
    font-size: 35px;
    font-weight: 900;
    letter-spacing: 1px;
    line-height: 52px;
    padding-left: 22px;
    text-transform: uppercase;
  }

  .amenities {
    position: absolute;
    left: 0; top: 525px;
    width: 1200px; height: 75px;
    background: var(--navy);
    display: flex;
    align-items: center;
    justify-content: center;
    gap: 24px;
    list-style: none;
    color: var(--white);
    font-size: 24px;
    font-weight: 900;
    letter-spacing: 0.5px;
    text-transform: uppercase;
  }
  .amenities li::before {
    content: "";
    display: inline-block;
    width: 12px; height: 12px;
    border-radius: 50%;
    background: var(--white);
    margin-right: 12px;
    vertical-align: middle;
    position: relative; top: -2px;
  }
  .direction-arrow { z-index: 2; }
</style>
</head>
<body>
  <main class="billboard">
    <span class="brand-mark" aria-hidden="true"></span>
    <h1 class="brand-name">
      <span class="line-main">COPPER RIDGE</span>
      <span class="line-sub">Resort &amp; Marina</span>
    </h1>

    <p class="phone">555-214-0867</p>

    <div class="lake-map" role="img" aria-label="Map outline of the lake"></div>

    <p class="distance">3 MILES</p>
    <div class="direction-stripes" aria-hidden="true"></div>
    <svg class="direction-arrow" width="70" height="112" viewBox="0 0 70 112" aria-hidden="true">
      <defs>
        <linearGradient id="arrowFill" x1="0" y1="0" x2="1" y2="0">
          <stop offset="0" stop-color="#f8b824"/>
          <stop offset="1" stop-color="#f0912c"/>
        </linearGradient>
      </defs>
      <polygon points="0,56 63,0 63,112" fill="url(#arrowFill)"/>
    </svg>
    <div class="web-bar">www.copperridgeresort.example</div>

    <ul class="amenities">
      <li>Lakefront Cabin Rentals</li>
      <li>Floating Vacation Homes</li>
      <li>New Slips Summer 2022</li>
    </ul>
  </main>
</body>
</html>
```